Announcement for a New Trauma Therapy Group - Rack Card

I need a two-sided "rack" card that is 4x9 announcing a Women's Trauma and Loss Group. I am a licensed therapist and will be starting this support group for women who have experienced trauma of all kinds. In addition to groups, I offer individual, couples, and family counseling sessions.

I would like to see designs that are soft tones and use colors like muted blues, greens, and sand tones. The final design should communicate hope and healing as well as have a peaceful feel to it.

I would like a picture of a woman's profile from either the side or from behind her. (possibly a contemplative picture on a beach)

I am attaching a picture of myself to go alongside the bio information as well.

On One Side, I need the description of the group and contact info:

Healing the Hurting Heart
Women's Trauma & Loss Group
Led by Licensed Professional Counselor, Joy Belden Crane

10 Week Group
Cost - $35 session
Group size limited to 10 participants

Topics Include:
What is Trauma?
How Trauma Affects Us
Creating a Feeling of Safety
Managing Trauma Triggers
Importance of Self Care
Healthy vs. Unhealthy Coping
Guilt, Shame, and Blame
Victim vs. Victimized
Grieving through Loss
Anger and Forgiveness
Imagining a Better Future

For More Information, Contact:
Joy Belden Crane, LPC, LMFT
(555) 614-3928
joy@brightmeadowcare.example

On Side Two:

Life hurts and does not seem fair. So what do you do when you are faced with an event in your life that knocks you off your feet? It seems no one understands what you are feeling and no one knows just what to say. It is tempting to pull away and isolate or put up a mask and pretend everything is OK.

It is my desire you know that you are not alone! There are others who understand the feelings you are going through and offer a safe place for encouraging support. I want to invite you to embark on a courageous journey of healing where you will not only learn how to "survive" after trauma and loss, but instead, learn that you can once again "thrive"!
- Joy Belden Crane, LPC, LMFT

Joy Belden Crane is a Licensed Professional Counselor and Licensed Marriage and Family Therapist. She is the owner of Still Waters Counseling Services located in Tulsa, OK.

Joy is a trauma survivor herself and understands firsthand the unique challenges that can arise on the journey to healing.

(Include Joy's picture next to bio)

(Attach logo and business information to this side as well.)

Target Market(s)

Women who have gone through a traumatic experience or loss and are hurting emotionally

Industry/Entity Type

Counsellor

Font styles to use
Serif
Script

Colors
fbe7d2
86cfc6
cfeae6
85abd2
cfdeed

Requirements
Must have
• Joy's picture as well as her logo and contact information must be on the card.
• One side of the card should describe the group with the following description:
• "Healing the Hurting Heart"
• Women's Trauma & Loss Group
• Led by Licensed Professional Counselor, Joy Belden Crane
• 10 Week Group
• Cost - $35 session
• Group size limited to 10 participants
• Topics Include:
• What is Trauma?
• How Trauma Affects Us
• Creating a Feeling of Safety
• Managing Trauma Triggers
• Importance of Self Care
• Healthy vs. Unhealthy Coping
• Guilt, Shame, and Blame
• Victim vs. Victimized
• Grieving through Loss
• Anger and Forgiveness
• Imagining a Better Future
• For More Information, Contact:
• Joy Belden Crane, LPC, LMFT
• (555) 614-3928
• joy@brightmeadowcare.example
• On the second side, it must have this note from Joy:
• Life hurts and does not seem fair. So what do you do when you are faced with an event in your life that knocks you off your feet? It seems no one understands what you are feeling and no one knows just what to say. It is tempting to pull away and isolate or put up a mask and pretend everything is OK.
• It is my desire you know that you are not alone! There are others who understand the feelings you are going through and offer a safe place for encouraging support. I want to invite you to embark on a courageous journey of healing where you will not only learn how to "survive" after trauma and loss, but instead, learn that you can once again "thrive"!
• - Joy Belden Crane, LPC, LMFT
• Joy Belden Crane is a Licensed Professional Counselor and Licensed Marriage and Family Therapist. She is the owner of Still Waters Counseling Services located in Tulsa, OK.
• Joy is a trauma survivor herself and understands firsthand the unique challenges that can arise on the journey to healing. In addition to facilitating groups, Joy also offers individual, marriage, and family counseling.
Nice to have
• soft muted colors that are peaceful. Light blues, greens, sand colors would work well. A picture at the top of the card of either a woman or a woman's profile that is hopeful such as a woman sitting at a beach overlooking the ocean.
Should not have
• No harsh or bright bold colors. This card needs to have a peaceful feeling to it.

```html
<!DOCTYPE html>
<html lang="en">
<head>
<meta charset="utf-8">
<title>Healing the Hurting Heart – Rack Card</title>
<link rel="stylesheet" href="https://fonts.googleapis.com/css2?family=League+Gothic&family=Oswald:wght@500&family=Jost:wght@400;500;600&family=Lato:wght@300;400&display=swap">
<style>
  :root {
    --stage: #727376;
    --cream: #f8ede2;
    --paper: #f5f5f3;
    --sage: #9bcaa9;
    --forest: #4b7a3b;
    --slate: #8b8b8d;
    --ink: #3a3a3a;
    --body-grey: #6f6f6f;
    --mist: #a9c3d6;
    --white: #ffffff;
  }
  * { box-sizing: border-box; margin: 0; padding: 0; }
  html, body { width: 1034px; height: 1200px; overflow: hidden; }
  body { background: var(--stage); position: relative; font-family: "Jost", sans-serif; }

  .card { position: absolute; top: 186px; width: 368px; height: 828px; overflow: hidden; background: var(--paper); }
  .card--front { left: 118px; }
  .card--back { left: 542px; }

  /* front */
  .hero { position: absolute; left: 0; top: 0; width: 368px; height: 513px;
    background: linear-gradient(180deg, #f8ede2 0%, #f3e6d8 45%, #d9d2c8 62%, #8f8c86 80%, #6d6e6c 100%); }
  .accent-bar { position: absolute; left: 0; top: 29px; width: 16px; height: 147px; background: #979797; }

  .brand { position: absolute; display: flex; align-items: center; gap: 7px;
    font-family: "Jost", sans-serif; font-weight: 500; color: var(--forest); line-height: 1.05; white-space: nowrap; }
  .brand__dot { width: 14px; height: 14px; border-radius: 50%; background: var(--forest); flex: none; }
  .brand--front { left: 36px; top: 74px; font-size: 17px; }
  .brand--back { left: 118px; top: 702px; font-size: 17px; }

  .title { position: absolute; left: 200px; top: 28px; width: 152px; font-family: "League Gothic", sans-serif;
    font-weight: 400; line-height: 0.9; white-space: nowrap; }
  .title span { display: block; }
  .title__a { color: var(--slate); font-size: 40px; }
  .title__b { color: var(--forest); font-size: 58px; }
  .title__c { color: var(--slate); font-size: 80px; }

  .group-name { position: absolute; left: 201px; top: 204px; font-family: "Oswald", sans-serif; font-weight: 500;
    color: #7f7f80; font-size: 16px; line-height: 1.3; white-space: nowrap; }
  .leader { position: absolute; left: 201px; top: 254px; font-family: "Oswald", sans-serif; font-weight: 500;
    color: #7f7f80; font-size: 12px; line-height: 1.5; white-space: nowrap; }
  .leader__name { font-size: 15px; }

  .facts { position: absolute; top: 466px; left: 0; width: 368px; height: 92px; }
  .fact { position: absolute; top: 0; width: 92px; height: 92px; border-radius: 50%; background: var(--forest);
    border: 3px solid var(--white); color: var(--white); display: flex; flex-direction: column;
    align-items: center; justify-content: center; text-align: center; line-height: 1.1; }
  .fact--weeks { left: 33px; font-size: 16px; }
  .fact--cost { left: 135px; font-size: 16px; }
  .fact--cost .fact__price { font-size: 22px; font-weight: 500; }
  .fact--cost .fact__unit { font-size: 10px; }
  .fact--size { left: 236px; font-size: 11px; }

  .topics-label { position: absolute; left: 81px; top: 579px; width: 219px; height: 24px; background: var(--sage);
    color: var(--white); font-weight: 500; font-size: 15px; letter-spacing: 5px; text-align: center; line-height: 24px; }
  .topics { position: absolute; top: 620px; list-style: none; font-size: 10.5px; color: #555; }
  .topics li { position: relative; padding-left: 13px; line-height: 12px; margin-bottom: 4.8px; }
  .topics li svg { position: absolute; left: 0; top: 2px; }
  .topics--left { left: 29px; width: 160px; }
  .topics--right { left: 200px; width: 160px; }

  .contact-lead { position: absolute; left: 0; width: 368px; top: 741px; text-align: center; font-size: 10.5px; color: #777; }
  .contact-name { position: absolute; left: 0; width: 368px; top: 756px; text-align: center; font-size: 14px; color: #6a6a6a; }
  .contact-name b { font-weight: 600; }

  .footer { position: absolute; left: 0; bottom: 0; width: 368px; height: 50px; background: var(--sage); color: var(--white); text-align: center; }
  .footer__phone { margin-top: 6px; font-size: 18px; font-weight: 600; display: flex; justify-content: center; align-items: center; gap: 3px; }
  .footer__mail { font-size: 11px; letter-spacing: 1.4px; display: flex; justify-content: center; align-items: center; gap: 4px; }

  /* back */
  .note-band { position: absolute; left: 0; top: 0; width: 368px; height: 392px; background: var(--sage); }
  .quote-mark { position: absolute; left: 0; width: 368px; top: 44px; text-align: center; color: var(--white);
    font-family: "Lato", sans-serif; font-size: 48px; font-weight: 400; line-height: 1; }
  .note { position: absolute; left: 38px; width: 292px; color: var(--white); font-family: "Lato", sans-serif;
    font-weight: 400; font-size: 11.4px; line-height: 15.4px; text-align: justify; }
  .note--one { top: 82px; }
  .note--two { top: 189px; }

  .portrait { position: absolute; left: 106px; top: 325px; width: 154px; height: 154px; border-radius: 50%;
    border: 3px solid var(--white); background: radial-gradient(circle at 50% 40%, #b8aa9a 0%, #8c7e70 55%, #5d5a58 100%); }
  .bio-name { position: absolute; left: 0; width: 368px; top: 490px; text-align: center; font-family: "Lato", sans-serif;
    font-size: 14px; color: var(--ink); }
  .bio-creds { position: absolute; left: 0; width: 368px; top: 510px; text-align: center; font-family: "Lato", sans-serif;
    font-size: 9px; line-height: 13px; color: var(--ink); }
  .divider { position: absolute; left: 152px; top: 546px; width: 64px; height: 2px; background: var(--mist); }
  .bio { position: absolute; left: 40px; width: 290px; font-family: "Lato", sans-serif; font-weight: 400;
    font-size: 11.6px; line-height: 15.5px; color: var(--body-grey); text-align: justify; }
  .bio--one { top: 563px; }
  .bio--two { top: 640px; }
</style>
</head>
<body>

<section class="card card--front">
  <div class="hero" role="img" aria-label="Photo of a woman seen from behind, sitting on a bench looking out over the sea"></div>
  <div class="accent-bar"></div>

  <div class="brand brand--front"><span class="brand__dot"></span><span>Still Waters<br>Counseling</span></div>

  <h1 class="title">
    <span class="title__a">HEALING THE</span>
    <span class="title__b">HURTING</span>
    <span class="title__c">HEART</span>
  </h1>

  <h2 class="group-name">WOMEN'S TRAUMA<br>&amp; LOSS GROUP</h2>
  <p class="leader">Led by Licensed<br>Professional Counselor,<br><span class="leader__name">Joy Belden Crane</span></p>

  <div class="facts">
    <div class="fact fact--weeks"><span>10 Week</span><span>Group</span></div>
    <div class="fact fact--cost"><span>Cost</span><span class="fact__price">$35</span><span class="fact__unit">session</span></div>
    <div class="fact fact--size"><span>Group size</span><span>limited to</span><span>10 participants</span></div>
  </div>

  <div class="topics-label">TOPICS INCLUDE</div>

  <ul class="topics topics--left">
    <li><svg width="8" height="8" viewBox="0 0 8 8"><circle cx="4" cy="4" r="3.4" fill="none" stroke="#4b7a3b" stroke-width=".8"/><path d="M2.3 4.1l1.2 1.2 2.3-2.5" fill="none" stroke="#4b7a3b" stroke-width=".9"/></svg>What is Trauma?</li>
    <li><svg width="8" height="8" viewBox="0 0 8 8"><circle cx="4" cy="4" r="3.4" fill="none" stroke="#4b7a3b" stroke-width=".8"/><path d="M2.3 4.1l1.2 1.2 2.3-2.5" fill="none" stroke="#4b7a3b" stroke-width=".9"/></svg>How Trauma Affects Us</li>
    <li><svg width="8" height="8" viewBox="0 0 8 8"><circle cx="4" cy="4" r="3.4" fill="none" stroke="#4b7a3b" stroke-width=".8"/><path d="M2.3 4.1l1.2 1.2 2.3-2.5" fill="none" stroke="#4b7a3b" stroke-width=".9"/></svg>Creating a Feeling of Safety</li>
    <li><svg width="8" height="8" viewBox="0 0 8 8"><circle cx="4" cy="4" r="3.4" fill="none" stroke="#4b7a3b" stroke-width=".8"/><path d="M2.3 4.1l1.2 1.2 2.3-2.5" fill="none" stroke="#4b7a3b" stroke-width=".9"/></svg>Managing Trauma Triggers</li>
    <li><svg width="8" height="8" viewBox="0 0 8 8"><circle cx="4" cy="4" r="3.4" fill="none" stroke="#4b7a3b" stroke-width=".8"/><path d="M2.3 4.1l1.2 1.2 2.3-2.5" fill="none" stroke="#4b7a3b" stroke-width=".9"/></svg>Importance of Self Care</li>
    <li><svg width="8" height="8" viewBox="0 0 8 8"><circle cx="4" cy="4" r="3.4" fill="none" stroke="#4b7a3b" stroke-width=".8"/><path d="M2.3 4.1l1.2 1.2 2.3-2.5" fill="none" stroke="#4b7a3b" stroke-width=".9"/></svg>Healthy vs. Unhealthy<br>Coping</li>
  </ul>
  <ul class="topics topics--right">
    <li><svg width="8" height="8" viewBox="0 0 8 8"><circle cx="4" cy="4" r="3.4" fill="none" stroke="#4b7a3b" stroke-width=".8"/><path d="M2.3 4.1l1.2 1.2 2.3-2.5" fill="none" stroke="#4b7a3b" stroke-width=".9"/></svg>Guilt, Shame, and Blame</li>
    <li><svg width="8" height="8" viewBox="0 0 8 8"><circle cx="4" cy="4" r="3.4" fill="none" stroke="#4b7a3b" stroke-width=".8"/><path d="M2.3 4.1l1.2 1.2 2.3-2.5" fill="none" stroke="#4b7a3b" stroke-width=".9"/></svg>Victim vs. Victimized</li>
    <li><svg width="8" height="8" viewBox="0 0 8 8"><circle cx="4" cy="4" r="3.4" fill="none" stroke="#4b7a3b" stroke-width=".8"/><path d="M2.3 4.1l1.2 1.2 2.3-2.5" fill="none" stroke="#4b7a3b" stroke-width=".9"/></svg>Grieving through Loss</li>
    <li><svg width="8" height="8" viewBox="0 0 8 8"><circle cx="4" cy="4" r="3.4" fill="none" stroke="#4b7a3b" stroke-width=".8"/><path d="M2.3 4.1l1.2 1.2 2.3-2.5" fill="none" stroke="#4b7a3b" stroke-width=".9"/></svg>Anger and Forgiveness</li>
    <li><svg width="8" height="8" viewBox="0 0 8 8"><circle cx="4" cy="4" r="3.4" fill="none" stroke="#4b7a3b" stroke-width=".8"/><path d="M2.3 4.1l1.2 1.2 2.3-2.5" fill="none" stroke="#4b7a3b" stroke-width=".9"/></svg>Imagining a Better Future</li>
  </ul>

  <p class="contact-lead">For More Information, Contact</p>
  <p class="contact-name"><b>Joy Belden Crane,</b> LPC, LMFT</p>

  <footer class="footer">
    <div class="footer__phone"><svg width="11" height="15" viewBox="0 0 11 15"><path d="M3 1c-1.5.6-2.3 2-2 4 .6 3.6 2.8 7 5.5 8.6 1.2.7 2.4.4 3.2-.5l-2-2.6c-.5.3-1 .4-1.5 0-1-1-1.8-2.8-2-4.2 0-.5.3-.9.8-1.1L3 1z" fill="#fff"/></svg>(555) 614-3928</div>
    <div class="footer__mail"><svg width="9" height="6" viewBox="0 0 9 6"><rect width="9" height="6" fill="#fff"/><path d="M0 0l4.5 3.4L9 0" fill="none" stroke="#9bcaa9" stroke-width=".8"/></svg>joy@brightmeadowcare.example</div>
  </footer>
</section>

<section class="card card--back">
  <div class="note-band"></div>
  <div class="quote-mark">&ldquo;</div>
  <p class="note note--one">Life hurts and does not seem fair. So what do you do when you are faced with an event in your life that knocks you off your feet? It seems no one understands what you are feeling and no one knows just what to say. It is tempting to pull away and isolate or put up a mask and pretend everything is OK.</p>
  <p class="note note--two">It is my desire you know that you are not alone! There are others who understand the feelings you are going through and offer a safe place for encouraging support. I want to invite you to embark on a courageous journey of healing where you will not only learn how to "survive" after trauma and loss, but instead, learn that you can once again "thrive"!</p>

  <div class="portrait" role="img" aria-label="Portrait photo of Joy Belden Crane sitting on a beach"></div>

  <p class="bio-name">Joy Belden Crane, LPC, LMFT</p>
  <p class="bio-creds">Licensed Professional Counselor<br>Licensed Marriage and Family Therapist</p>
  <div class="divider"></div>

  <p class="bio bio--one">Joy Belden Crane is a Licensed Professional Counselor and Licensed Marriage and Family Therapist. She is the owner of Still Waters Counseling Services located in Tulsa, OK.</p>
  <p class="bio bio--two">Joy is a trauma survivor herself and understands firsthand the unique challenges that can arise on the journey to healing.</p>

  <div class="brand brand--back"><span class="brand__dot"></span><span>Still Waters<br>Counseling</span></div>

  <footer class="footer">
    <div class="footer__phone"><svg width="11" height="15" viewBox="0 0 11 15"><path d="M3 1c-1.5.6-2.3 2-2 4 .6 3.6 2.8 7 5.5 8.6 1.2.7 2.4.4 3.2-.5l-2-2.6c-.5.3-1 .4-1.5 0-1-1-1.8-2.8-2-4.2 0-.5.3-.9.8-1.1L3 1z" fill="#fff"/></svg>(555) 614-3928</div>
    <div class="footer__mail"><svg width="9" height="6" viewBox="0 0 9 6"><rect width="9" height="6" fill="#fff"/><path d="M0 0l4.5 3.4L9 0" fill="none" stroke="#9bcaa9" stroke-width=".8"/></svg>joy@brightmeadowcare.example</div>
  </footer>
</section>

</body>
</html>
```